Communication and Marketing agency needs a new presentation card

We are a group of communication and marketing agencies specialized in companies that are in the logistics and industrial sector. The head agency is TELVANO Grupo and the group consists of 4 agencies: TELVANO Media, TELVANO Digital, TELVANO Research and EnlazaPorImagen. We hace 4 offices in Spain (Madrid, Barcelona, Valencia and Murcia). We are looking for a clean and attractive design that transmits our experience, brand presence in the market and knowledge to those who receive the card.It has to maintain the colors of the logo that is attached.
Target Market(s)
logistics and industrial sector
Marketing department
Clean and attractive design

```html
<!DOCTYPE html>
<html lang="en">
<head>
<meta charset="utf-8">
<title>Business Card Design – EnlazaPorImagen</title>
<link rel="stylesheet" href="https://fonts.googleapis.com/css2?family=Roboto:ital,wght@0,300;0,400;0,500;1,300;1,400&display=swap">
<style>
  :root{
    --red:#b01e2a;
    --dark:#2e2927;
    --paper:#f1f1f1;
    --bg:#ebebeb;
    --ink:#2b2b2b;
    --white:#ffffff;
    --line:rgba(255,255,255,.55);
  }
  *{box-sizing:border-box;margin:0;padding:0}
  html,body{width:1200px;height:3464px;overflow:hidden}
  body{position:relative;background:var(--bg);font-family:"Roboto",Arial,sans-serif;color:var(--ink)}

  .backdrop{position:absolute;inset:0;width:1200px;height:3464px}
  .fill-red{fill:var(--red)}
  .fill-dark{fill:var(--dark)}
  .fill-paper{fill:var(--paper)}
  .rule{stroke:var(--line);stroke-width:1}

  /* header */
  .title{position:absolute;left:68px;top:92px;font-weight:400;line-height:1;text-transform:uppercase}
  .title .l1{display:block;font-size:66px;color:var(--ink);letter-spacing:.5px}
  .title .l2{display:block;font-size:66px;color:var(--red);font-weight:500;margin-top:20px}
  .specs{position:absolute;left:74px;top:296px;list-style:none}
  .specs li{display:flex;align-items:center;height:74px;font-size:34px;text-transform:uppercase;color:var(--ink)}
  .specs li::before{content:"";width:28px;height:28px;background:var(--red);margin-right:34px}

  /* features */
  .features{position:absolute;left:0;top:948px;width:1200px;height:200px}
  .feature{position:absolute;width:220px;margin-left:-110px;text-align:center;color:var(--white)}
  .feature svg{display:block;margin:0 auto;width:88px;height:88px}
  .feature span{display:block;margin-top:28px;font-size:25px;line-height:1.3;text-transform:uppercase}

  /* tagline */
  .tagline{position:absolute;left:0;top:2566px;width:1200px;text-align:center;font-size:33px;color:#111;text-transform:uppercase;letter-spacing:.5px}
  .tagline b{font-weight:500}
  .tagline .sep{margin:0 18px;font-weight:300}

  /* cards */
  .card{position:absolute;overflow:hidden;container-type:inline-size;background:var(--paper);box-shadow:10px 14px 22px rgba(0,0,0,.32)}
  .card .shapes{position:absolute;inset:0;width:100%;height:100%}

  .card .person{position:absolute;left:11%;top:19%;width:32%;text-align:center;color:var(--white);font-style:italic;font-weight:300;text-transform:uppercase;white-space:nowrap}
  .card .person .name{display:block;font-size:3.4cqw;line-height:1.1}
  .card .person .role{display:block;font-size:2.4cqw;margin-top:.4cqw}
  .card .contacts{position:absolute;left:19.5%;top:40%;list-style:none;color:var(--white);font-style:italic;font-weight:300;font-size:2.4cqw;line-height:1.25;white-space:nowrap}
  .card .contacts li{margin-bottom:1.8cqw}
  .card .contact-tab{position:absolute;left:9%;top:37%;width:5.5%;height:46%}

  .card .brand{position:absolute;color:var(--red);font-weight:300;font-size:5.8cqw;line-height:1.05;text-transform:uppercase;white-space:nowrap}
  .card .brand span{display:block}
  .card.front .brand{left:55%;top:39%}
  .card.back .brand{left:8.5%;top:37%}

  .card .agencies{position:absolute;right:25%;top:50%;list-style:none;text-align:right}
  .card .agencies li{height:5.6cqw;display:flex;align-items:center;justify-content:flex-end;font-size:1.9cqw;line-height:1;color:var(--white);font-weight:500;text-transform:uppercase;white-space:nowrap}
</style>
</head>
<body>

<svg class="backdrop" viewBox="0 0 1200 3464" aria-hidden="true">
  <polygon class="fill-red" points="0,631 1200,334 1200,1163 0,2004"/>
</svg>

<h1 class="title"><span class="l1">Business</span><span class="l2">Card Design</span></h1>
<ul class="specs">
  <li>3.5 x 2 inches</li>
  <li>Adobe Illustration</li>
  <li>Fully editable</li>
  <li>Print ready</li>
  <li>300 DPI</li>
</ul>

<!-- top pair -->
<div class="card front" style="left:576px;top:104px;width:555px;height:322px">
  <svg class="shapes" viewBox="0 0 100 100" preserveAspectRatio="none" aria-hidden="true">
    <polygon class="fill-red" points="0,0 38,0 63,100 26,100"/>
    <polygon class="fill-dark" points="38,0 100,0 100,100 63,100"/>
  </svg>
  <svg class="contact-tab" viewBox="0 0 20 100" preserveAspectRatio="none" aria-hidden="true">
    <polygon class="fill-dark" points="4,0 20,0 20,100 12,100 0,80 0,5"/>
    <circle cx="10" cy="14" r="3.6" fill="#fff"/><circle cx="10" cy="38" r="3.6" fill="#fff"/><circle cx="10" cy="62" r="3.6" fill="#fff"/><circle cx="10" cy="84" r="3.6" fill="#fff"/>
  </svg>
  <div class="person"><span class="name">Marco Delgado</span><span class="role">Director</span></div>
  <ul class="contacts"><li>0522 48 90317</li><li>hola@enlazaporimagen.com</li><li>www.enlazaporimagen.com</li><li>214/36 harbour lane,<br>valencia 46001</li></ul>
  <div class="brand"><span>EnlazaPor</span><span>Imagen</span></div>
</div>
<div class="card back" style="left:574px;top:477px;width:557px;height:330px">
  <svg class="shapes" viewBox="0 0 100 100" preserveAspectRatio="none" aria-hidden="true">
    <polygon class="fill-dark" points="0,0 100,0 100,100 0,100"/>
    <polygon class="fill-red" points="68,0 92,0 74,100 47,100"/>
    <polygon class="fill-paper" points="92,0 100,0 100,100 74,100"/>
    <line class="rule" x1="47" y1="60" x2="80" y2="60" vector-effect="non-scaling-stroke"/>
    <line class="rule" x1="47" y1="69.5" x2="78" y2="69.5" vector-effect="non-scaling-stroke"/>
    <line class="rule" x1="47" y1="79" x2="76.5" y2="79" vector-effect="non-scaling-stroke"/>
  </svg>
  <div class="brand"><span>EnlazaPor</span><span>Imagen</span></div>
  <ul class="agencies"><li>Telvano Digital</li><li>Telvano Media</li><li>Telvano Grupo</li><li>Telvano Research</li></ul>
</div>

<!-- feature row -->
<div class="features">
  <div class="feature" style="left:141px">
    <svg viewBox="0 0 48 48" fill="none" stroke="#fff" stroke-width="2.2" stroke-linejoin="round" stroke-linecap="round" aria-hidden="true">
      <path d="M8 4h20l8 8v30H8z"/><path d="M28 4v8h8"/><path d="M14 18h14M14 24h14M14 30h8"/><path d="M40 18l4 4-14 14-5 1 1-5z"/>
    </svg>
    <span>3.5 x 2 inches<br>with bleed</span>
  </div>
  <div class="feature" style="left:366px">
    <svg viewBox="0 0 48 48" fill="none" stroke="#fff" stroke-width="2.2" stroke-linejoin="round" aria-hidden="true">
      <path d="M14 4h20v12H14z"/><rect x="4" y="16" width="40" height="18" rx="4"/><path d="M14 28h20v16H14z"/><path d="M18 34h12M18 39h12"/>
    </svg>
    <span>Print<br>ready</span>
  </div>
  <div class="feature" style="left:574px">
    <svg viewBox="0 0 48 48" fill="none" stroke="#fff" stroke-width="2.2" stroke-linejoin="round" aria-hidden="true">
      <path d="M16 4h22v34"/><rect x="10" y="10" width="22" height="34" rx="1"/>
    </svg>
    <span>Fully<br>editable</span>
  </div>
  <div class="feature" style="left:816px;top:-14px">
    <svg viewBox="0 0 48 48" fill="none" stroke="#fff" stroke-width="2.2" aria-hidden="true">
      <rect x="4" y="6" width="10" height="8" rx="2"/><rect x="18" y="6" width="26" height="8" rx="2"/>
      <rect x="4" y="20" width="10" height="8" rx="2"/><rect x="18" y="20" width="26" height="8" rx="2"/>
      <rect x="4" y="34" width="10" height="8" rx="2"/><rect x="18" y="34" width="26" height="8" rx="2"/>
    </svg>
    <span>Layer<br>&amp; organized</span>
  </div>
  <div class="feature" style="left:1034px">
    <svg viewBox="0 0 48 48" fill="none" stroke="#fff" stroke-width="2.2" stroke-linejoin="round" stroke-linecap="round" aria-hidden="true">
      <path d="M18 4h12M20 4v14L8 40a3 3 0 0 0 3 4h26a3 3 0 0 0 3-4L28 18V4"/><path d="M13 32h22"/><circle cx="22" cy="37" r="1.5"/><circle cx="28" cy="26" r="1.5"/>
    </svg>
    <span>Professional<br>design</span>
  </div>
</div>

<!-- large pair -->
<div class="card front" style="left:153px;top:1244px;width:896px;height:532px">
  <svg class="shapes" viewBox="0 0 100 100" preserveAspectRatio="none" aria-hidden="true">
    <polygon class="fill-red" points="0,0 38,0 63,100 26,100"/>
    <polygon class="fill-dark" points="38,0 100,0 100,100 63,100"/>
  </svg>
  <svg class="contact-tab" viewBox="0 0 20 100" preserveAspectRatio="none" aria-hidden="true">
    <polygon class="fill-dark" points="4,0 20,0 20,100 12,100 0,80 0,5"/>
    <circle cx="10" cy="14" r="3.6" fill="#fff"/><circle cx="10" cy="38" r="3.6" fill="#fff"/><circle cx="10" cy="62" r="3.6" fill="#fff"/><circle cx="10" cy="84" r="3.6" fill="#fff"/>
  </svg>
  <div class="person"><span class="name">Marco Delgado</span><span class="role">Director</span></div>
  <ul class="contacts"><li>0522 48 90317</li><li>hola@enlazaporimagen.com</li><li>www.enlazaporimagen.com</li><li>214/36 harbour lane,<br>valencia 46001</li></ul>
  <div class="brand"><span>EnlazaPor</span><span>Imagen</span></div>
</div>
<div class="card back" style="left:153px;top:1856px;width:896px;height:532px">
  <svg class="shapes" viewBox="0 0 100 100" preserveAspectRatio="none" aria-hidden="true">
    <polygon class="fill-dark" points="0,0 100,0 100,100 0,100"/>
    <polygon class="fill-red" points="68,0 92,0 74,100 47,100"/>
    <polygon class="fill-paper" points="92,0 100,0 100,100 74,100"/>
    <line class="rule" x1="47" y1="60" x2="80" y2="60" vector-effect="non-scaling-stroke"/>
    <line class="rule" x1="47" y1="69.5" x2="78" y2="69.5" vector-effect="non-scaling-stroke"/>
    <line class="rule" x1="47" y1="79" x2="76.5" y2="79" vector-effect="non-scaling-stroke"/>
  </svg>
  <div class="brand"><span>EnlazaPor</span><span>Imagen</span></div>
  <ul class="agencies"><li>Telvano Digital</li><li>Telvano Media</li><li>Telvano Grupo</li><li>Telvano Research</li></ul>
</div>

<p class="tagline"><b>Professional</b> design<span class="sep">|</span><b>Business</b> card</p>

<!-- thumbnail grid -->
<div class="card back" style="left:74px;top:2816px;width:314px;height:154px">
  <svg class="shapes" viewBox="0 0 100 100" preserveAspectRatio="none" aria-hidden="true">
    <polygon class="fill-dark" points="0,0 100,0 100,100 0,100"/>
    <polygon class="fill-red" points="68,0 92,0 74,100 47,100"/>
    <polygon class="fill-paper" points="92,0 100,0 100,100 74,100"/>
    <line class="rule" x1="47" y1="60" x2="80" y2="60" vector-effect="non-scaling-stroke"/>
    <line class="rule" x1="47" y1="69.5" x2="78" y2="69.5" vector-effect="non-scaling-stroke"/>
    <line class="rule" x1="47" y1="79" x2="76.5" y2="79" vector-effect="non-scaling-stroke"/>
  </svg>
  <div class="brand"><span>EnlazaPor</span><span>Imagen</span></div>
  <ul class="agencies"><li>Telvano Digital</li><li>Telvano Media</li><li>Telvano Grupo</li><li>Telvano Research</li></ul>
</div>
<div class="card front" style="left:403px;top:2771px;width:396px;height:235px">
  <svg class="shapes" viewBox="0 0 100 100" preserveAspectRatio="none" aria-hidden="true">
    <polygon class="fill-red" points="0,0 38,0 63,100 26,100"/>
    <polygon class="fill-dark" points="38,0 100,0 100,100 63,100"/>
  </svg>
  <svg class="contact-tab" viewBox="0 0 20 100" preserveAspectRatio="none" aria-hidden="true">
    <polygon class="fill-dark" points="4,0 20,0 20,100 12,100 0,80 0,5"/>
    <circle cx="10" cy="14" r="3.6" fill="#fff"/><circle cx="10" cy="38" r="3.6" fill="#fff"/><circle cx="10" cy="62" r="3.6" fill="#fff"/><circle cx="10" cy="84" r="3.6" fill="#fff"/>
  </svg>
  <div class="person"><span class="name">Marco Delgado</span><span class="role">Director</span></div>
  <ul class="contacts"><li>0522 48 90317</li><li>hola@enlazaporimagen.com</li><li>www.enlazaporimagen.com</li><li>214/36 harbour lane,<br>valencia 46001</li></ul>
  <div class="brand"><span>EnlazaPor</span><span>Imagen</span></div>
</div>
<div class="card back" style="left:816px;top:2816px;width:315px;height:154px">
  <svg class="shapes" viewBox="0 0 100 100" preserveAspectRatio="none" aria-hidden="true">
    <polygon class="fill-dark" points="0,0 100,0 100,100 0,100"/>
    <polygon class="fill-red" points="68,0 92,0 74,100 47,100"/>
    <polygon class="fill-paper" points="92,0 100,0 100,100 74,100"/>
    <line class="rule" x1="47" y1="60" x2="80" y2="60" vector-effect="non-scaling-stroke"/>
    <line class="rule" x1="47" y1="69.5" x2="78" y2="69.5" vector-effect="non-scaling-stroke"/>
    <line class="rule" x1="47" y1="79" x2="76.5" y2="79" vector-effect="non-scaling-stroke"/>
  </svg>
  <div class="brand"><span>EnlazaPor</span><span>Imagen</span></div>
  <ul class="agencies"><li>Telvano Digital</li><li>Telvano Media</li><li>Telvano Grupo</li><li>Telvano Research</li></ul>
</div>

<div class="card front" style="left:74px;top:3031px;width:314px;height:186px">
  <svg class="shapes" viewBox="0 0 100 100" preserveAspectRatio="none" aria-hidden="true">
    <polygon class="fill-red" points="0,0 38,0 63,100 26,100"/>
    <polygon class="fill-dark" points="38,0 100,0 100,100 63,100"/>
  </svg>
  <svg class="contact-tab" viewBox="0 0 20 100" preserveAspectRatio="none" aria-hidden="true">
    <polygon class="fill-dark" points="4,0 20,0 20,100 12,100 0,80 0,5"/>
    <circle cx="10" cy="14" r="3.6" fill="#fff"/><circle cx="10" cy="38" r="3.6" fill="#fff"/><circle cx="10" cy="62" r="3.6" fill="#fff"/><circle cx="10" cy="84" r="3.6" fill="#fff"/>
  </svg>
  <div class="person"><span class="name">Marco Delgado</span><span class="role">Director</span></div>
  <ul class="contacts"><li>0522 48 90317</li><li>hola@enlazaporimagen.com</li><li>www.enlazaporimagen.com</li><li>214/36 harbour lane,<br>valencia 46001</li></ul>
  <div class="brand"><span>EnlazaPor</span><span>Imagen</span></div>
</div>
<div class="card back" style="left:403px;top:3017px;width:396px;height:233px">
  <svg class="shapes" viewBox="0 0 100 100" preserveAspectRatio="none" aria-hidden="true">
    <polygon class="fill-dark" points="0,0 100,0 100,100 0,100"/>
    <polygon class="fill-red" points="68,0 92,0 74,100 47,100"/>
    <polygon class="fill-paper" points="92,0 100,0 100,100 74,100"/>
    <line class="rule" x1="47" y1="60" x2="80" y2="60" vector-effect="non-scaling-stroke"/>
    <line class="rule" x1="47" y1="69.5" x2="78" y2="69.5" vector-effect="non-scaling-stroke"/>
    <line class="rule" x1="47" y1="79" x2="76.5" y2="79" vector-effect="non-scaling-stroke"/>
  </svg>
  <div class="brand"><span>EnlazaPor</span><span>Imagen</span></div>
  <ul class="agencies"><li>Telvano Digital</li><li>Telvano Media</li><li>Telvano Grupo</li><li>Telvano Research</li></ul>
</div>
<div class="card front" style="left:816px;top:3031px;width:315px;height:186px">
  <svg class="shapes" viewBox="0 0 100 100" preserveAspectRatio="none" aria-hidden="true">
    <polygon class="fill-red" points="0,0 38,0 63,100 26,100"/>
    <polygon class="fill-dark" points="38,0 100,0 100,100 63,100"/>
  </svg>
  <svg class="contact-tab" viewBox="0 0 20 100" preserveAspectRatio="none" aria-hidden="true">
    <polygon class="fill-dark" points="4,0 20,0 20,100 12,100 0,80 0,5"/>
    <circle cx="10" cy="14" r="3.6" fill="#fff"/><circle cx="10" cy="38" r="3.6" fill="#fff"/><circle cx="10" cy="62" r="3.6" fill="#fff"/><circle cx="10" cy="84" r="3.6" fill="#fff"/>
  </svg>
  <div class="person"><span class="name">Marco Delgado</span><span class="role">Director</span></div>
  <ul class="contacts"><li>0522 48 90317</li><li>hola@enlazaporimagen.com</li><li>www.enlazaporimagen.com</li><li>214/36 harbour lane,<br>valencia 46001</li></ul>
  <div class="brand"><span>EnlazaPor</span><span>Imagen</span></div>
</div>

</body>
</html>
```